We are a building company that build new homes and units we are looking for something fresh and looks good my company name is
Larkmoor Building Group Pty Ltd

Industry/Entity Type

Building

Contact Information for Business Card

Name Marco Delacruz-Fenn
Tittle: Director
Address 14 Quarrel St. Thornbury Vic 3071
Ph: 03 9612 4087
Mobile : 0400 562 938

www.larkmoorbuildinggroup.com.au
Email: sales@larkmoorbuildinggroup.com.au

```html
<!DOCTYPE html>
<html lang="en">
<head>
<meta charset="utf-8">
<title>Larkmoor Building Group Pty Ltd – Business Card</title>
<link href="https://fonts.googleapis.com/css2?family=Noto+Sans:wght@400;600&display=swap" rel="stylesheet">
<style>
  :root {
    --page: #e9eaec;
    --card-white: #ffffff;
    --card-black: #0b0b0b;
    --brand-blue: #1f72b9;
    --brand-grey: #7d7d7d;
    --light-grey: #a9a9a9;
    --text-white: #ffffff;
  }
  * { box-sizing: border-box; margin: 0; padding: 0; }
  html, body {
    width: 1200px; height: 900px; overflow: hidden;
    background: var(--page);
    font-family: "Noto Sans", Arial, sans-serif;
  }
  .sheet {
    width: 1200px; height: 900px;
    display: flex; flex-direction: column;
    align-items: center; justify-content: center; gap: 40px;
  }
  .card {
    position: relative;
    width: 700px; height: 400px;
    border-radius: 22px;
    overflow: hidden;
    box-shadow: 0 8px 24px rgba(0,0,0,0.18);
  }
  /* Back side */
  .card--back {
    background: var(--card-black);
    display: flex; align-items: center; justify-content: center;
  }
  .card--back .wordmark { color: var(--light-grey); }
  /* Front side */
  .card--front { background: var(--card-white); }
  .brand-block {
    position: absolute; left: 0; top: 0;
    width: 310px; height: 100%;
    display: flex; align-items: center; justify-content: center;
  }
  .wordmark {
    display: flex; align-items: center; gap: 12px;
    color: var(--brand-grey);
    font-weight: 600; font-size: 21px; line-height: 1.2;
  }
  .wordmark__square {
    width: 18px; height: 18px; flex: none;
    background: var(--brand-blue);
  }
  .wordmark__name { max-width: 230px; }
  .info-panel {
    position: absolute; left: 310px; top: 0;
    width: 350px; height: 100%;
    background: var(--brand-blue);
    color: var(--text-white);
  }
  .info-panel::before {
    content: ""; position: absolute;
    left: -12px; top: 88px;
    border-top: 12px solid transparent;
    border-bottom: 12px solid transparent;
    border-right: 12px solid var(--brand-blue);
  }
  .person { position: absolute; left: 26px; top: 62px; }
  .person__name { font-size: 25px; font-weight: 400; letter-spacing: -0.2px; white-space: nowrap; }
  .person__title { font-size: 16px; margin-left: 22px; margin-top: 2px; }
  .contacts {
    position: absolute; left: 26px; top: 222px;
    list-style: none;
  }
  .contacts li {
    display: flex; align-items: center; gap: 10px;
    font-size: 19px; line-height: 31px; white-space: nowrap;
  }
  .contacts li.contacts__small { font-size: 15px; }
  .contacts svg { width: 16px; height: 16px; flex: none; fill: var(--text-white); }
</style>
</head>
<body>
<main class="sheet">

  <section class="card card--back" aria-label="Card back">
    <div class="wordmark">
      <span class="wordmark__square"></span>
      <span class="wordmark__name">Larkmoor Building Group Pty Ltd</span>
    </div>
  </section>

  <section class="card card--front" aria-label="Card front">
    <div class="brand-block">
      <div class="wordmark">
        <span class="wordmark__square"></span>
        <span class="wordmark__name">Larkmoor Building Group Pty Ltd</span>
      </div>
    </div>

    <div class="info-panel">
      <div class="person">
        <p class="person__name">Marco Delacruz-Fenn</p>
        <p class="person__title">Title</p>
      </div>
      <ul class="contacts">
        <li>
          <svg viewBox="0 0 16 16" aria-hidden="true"><path d="M3.6 1.2l2.3 2.7-1.3 1.8c.9 2 2.5 3.6 4.5 4.6l1.8-1.3 2.7 2.3-1.4 2.4C7 13.4 2.4 8.8 1.2 3z"/></svg>
          03 9612 4087
        </li>
        <li>
          <svg viewBox="0 0 16 16" aria-hidden="true"><path d="M4 1h8v14H4z M5.5 2.5v5h5v-5z M5.5 9h1.5v1.3H5.5z M7.3 9h1.4v1.3H7.3z M9 9h1.5v1.3H9z M5.5 11h1.5v1.3H5.5z M7.3 11h1.4v1.3H7.3z M9 11h1.5v1.3H9z" fill-rule="evenodd"/></svg>
          0400 562 938
        </li>
        <li class="contacts__small">
          <svg viewBox="0 0 16 16" aria-hidden="true"><path d="M1 3.5h14v9H1z M2.5 4.5L8 8.8l5.5-4.3z" fill-rule="evenodd"/></svg>
          sales@larkmoorbuildinggroup.com.au
        </li>
        <li class="contacts__small">
          <svg viewBox="0 0 16 16" aria-hidden="true"><path d="M8 1a7 7 0 1 0 0 14A7 7 0 0 0 8 1zm0 1.3c.8 0 1.7 1.7 2 4.1H6c.3-2.4 1.2-4.1 2-4.1zM2.4 6.4c.4-1.8 1.6-3.2 3.2-3.8-.5 1-.8 2.3-.9 3.8zm8.9 0c-.1-1.5-.4-2.8-.9-3.8 1.6.6 2.8 2 3.2 3.8zM2.4 9.6h2.3c.1 1.5.4 2.8.9 3.8-1.6-.6-2.8-2-3.2-3.8zm3.6 0h4c-.3 2.4-1.2 4.1-2 4.1s-1.7-1.7-2-4.1zm5.3 0h2.3c-.4 1.8-1.6 3.2-3.2 3.8.5-1 .8-2.3.9-3.8zM6 7.6h4v.8H6z"/></svg>
          www.larkmoorbuildinggroup.com.au
        </li>
      </ul>
    </div>
  </section>

</main>
</body>
</html>
```